Business Card Design

We need a business card to highlight our property maintenance company. we specialize in commercial and industrial property maintenance. services include landscaping snow and ice management. janitorial services. cleanroom services. parking lot maintenance.
Updates
I have narrowed down to two designs thank you waiting on some minor changes to both designs to choose.
Target Market(s)
facility managers/property managers
Industry/Entity Type
Property Maintenance
Contact Information for Business Card
47 Brindlewood Rd.
Larkfield, Nh. 01839
978-552-3716
Look and feel

```html
<!DOCTYPE html>
<html lang="en">
<head>
<meta charset="utf-8">
<title>Keystone Facilities Services – Business Card</title>
<link rel="stylesheet" href="https://fonts.googleapis.com/css2?family=Questrial&family=Cinzel:wght@700&display=swap">
<style>
  :root {
    --navy: #15154a;
    --yellow: #fcc800;
    --white: #ffffff;
    --backdrop: #dedede;
    --text-font: "Questrial", sans-serif;
    --caps-font: "Cinzel", serif;
  }
  * { box-sizing: border-box; margin: 0; padding: 0; }
  html, body { width: 1200px; height: 900px; overflow: hidden; }
  body { background: var(--backdrop); position: relative; font-family: var(--text-font); }

  .card { position: absolute; overflow: hidden; }
  .card-front { left: 101px; top: 51px; width: 413px; height: 704px; background: var(--navy); }
  .card-back { left: 655px; top: 50px; width: 416px; height: 710px; background: var(--navy); }

  .front-wave { position: absolute; inset: 0; width: 100%; height: 100%; }

  .brand-name {
    position: absolute; left: 0; right: 0; top: 280px;
    display: flex; justify-content: center; align-items: center; gap: 14px;
    font-family: var(--text-font); font-size: 58px; line-height: 58px; color: var(--navy);
  }
  .brand-mark { width: 34px; height: 34px; background: var(--yellow); display: inline-block; }
  .brand-tagline {
    position: absolute; left: 0; right: 0; top: 352px; text-align: center; color: var(--navy);
    font-family: var(--caps-font); font-weight: 700;
    font-size: 34px; line-height: 38px; letter-spacing: 2px; font-variant: small-caps;
  }

  .contact { position: absolute; left: 36px; top: 565px; color: var(--white); font-size: 25px; line-height: 30.5px; font-style: normal; }
  .contact-line { display: flex; align-items: flex-start; white-space: nowrap; }
  .contact-icon { width: 31px; height: 30px; flex: none; display: flex; align-items: center; }
  .contact-indent { padding-left: 31px; }

  .services { position: absolute; left: 0; right: 0; top: 206px; text-align: center; font-size: 25px; line-height: 29.5px; }
  .services-lead { color: var(--yellow); }
  .services-list { margin-top: 30px; color: var(--white); list-style: none; }
</style>
</head>
<body>
  <section class="card card-front" aria-label="Business card front">
    <svg class="front-wave" viewBox="0 0 413 704" aria-hidden="true">
      <path d="M95 470 C230 510 350 480 413 400 V498 C330 540 200 520 95 470 Z" fill="var(--yellow)"/>
      <path d="M0 0 H413 V404 C340 470 220 500 100 465 C60 452 25 430 0 410 Z" fill="var(--white)"/>
    </svg>

    <div class="brand-name"><span class="brand-mark"></span>Keystone</div>
    <p class="brand-tagline">Facilities Services<br>Larkfield, Nh</p>

    <address class="contact">
      <div class="contact-line">
        <span class="contact-icon">
          <svg width="24" height="24" viewBox="0 0 24 24" aria-hidden="true"><path d="M6.6 10.8a15 15 0 0 0 6.6 6.6l2.2-2.2a1 1 0 0 1 1-.25 11.4 11.4 0 0 0 3.6.6 1 1 0 0 1 1 1V20a1 1 0 0 1-1 1A17 17 0 0 1 3 4a1 1 0 0 1 1-1h3.5a1 1 0 0 1 1 1c0 1.25.2 2.45.6 3.6a1 1 0 0 1-.25 1z" fill="var(--yellow)"/></svg>
        </span>
        <span>978-552-3716</span>
      </div>
      <div class="contact-line">
        <span class="contact-icon">
          <svg width="26" height="24" viewBox="0 0 26 24" aria-hidden="true"><path d="M13 2 1 12h3v10h6.5v-6h5v6H22V12h3z" fill="var(--yellow)"/></svg>
        </span>
        <span>47 Brindlewood Rd. Larkfield,</span>
      </div>
      <div class="contact-line contact-indent"><span>Nh. 01839</span></div>
    </address>
  </section>

  <section class="card card-back" aria-label="Business card back">
    <div class="services">
      <p class="services-lead">specialize in commercial and<br>industrial<br>property maintenance.</p>
      <ul class="services-list">
        <li>landscaping snow and ice<br>management.</li>
        <li>janitorial services.</li>
        <li>cleanroom services.</li>
        <li>parking lot maintenance.</li>
      </ul>
    </div>
  </section>
</body>
</html>
```